Label for high-end indie coffee package

I need a label for high-end indie coffee package.

Coffee comes from Mt. Elgon, Trans-Nzoia County, Kenya. The coffee will be sold in Finland. The package as such will be semi matte black and the label will be printed out as a sticker.

Maximum measurements for the label would around 9 x 9 centimeters. It can be a square / rectangle / circle. I would like it to include influences from coffee origins (Kenya) and also demonstrate the high-end quality of the coffee with the modern twist.

The label should include the following text:

Coffee Name:
Moruvi Kelano AA
Washed & Natural

Origins:
Mt. Elgon, Trans-Nzoia County, Kenya

Growing altitude:
Altitude: 1 800 amsl

Coffee variety:
100 % Arabica

Following fields should be possible to be filled afterwards when the need occurs:
roast date
best before
roasted by

I'll be more than happy to answer any questions!

Finland. High-end customers, design coffee shops.

```html
<!DOCTYPE html>
<html lang="en">
<head>
<meta charset="utf-8">
<title>Moruvi Kelano AA – Coffee Label</title>
<link rel="stylesheet" href="https://fonts.googleapis.com/css2?family=Oswald:wght@500;600&family=Roboto+Condensed:wght@400;700&display=swap">
<style>
  :root {
    --backdrop: #f4f4f4;
    --ink: #111111;
    --paper: #dcdcdc;
    --paper-light: #e6e6e6;
    --muted: #555555;
    --rule: #2a2a2a;
    --reverse: #f2f2f2;
  }
  * { margin: 0; padding: 0; box-sizing: border-box; }
  html, body {
    width: 1200px; height: 962px; overflow: hidden;
    background: var(--backdrop);
  }
  .label {
    position: absolute; left: 207px; top: 51px;
    width: 786px; height: 860px;
    background: var(--ink);
    padding: 46px;
  }
  .sticker {
    position: relative; width: 100%; height: 100%;
    border-radius: 46px;
    overflow: hidden;
    background: radial-gradient(circle at 40% 30%, var(--paper-light), var(--paper));
    color: var(--ink);
  }
  .branch-illustration {
    position: absolute; left: 40px; top: 70px;
    width: 240px; height: 380px;
    border-radius: 40px;
    background: linear-gradient(160deg, #c9c9c9, #a9a9a9);
  }
  .product-name {
    position: absolute; left: 300px; top: 50px;
    font-family: "Oswald", sans-serif; font-weight: 600;
    font-size: 108px; line-height: 100px;
    text-transform: uppercase; letter-spacing: 0;
    white-space: nowrap;
  }
  .process-tag {
    position: absolute; left: 462px; top: 262px;
    width: 190px; height: 104px;
    background: var(--ink); color: var(--reverse);
    font-family: "Oswald", sans-serif; font-weight: 500;
    font-size: 32px; line-height: 38px; text-transform: uppercase;
    display: flex; flex-direction: column; justify-content: center;
    padding-left: 14px;
  }
  .details {
    position: absolute; left: 130px; right: 0; top: 440px;
    height: 280px;
    border-top: 3px solid var(--rule);
    display: flex;
    font-family: "Roboto Condensed", sans-serif;
  }
  .details-origin { width: 366px; padding-top: 40px; border-right: 3px solid var(--rule); }
  .details-roast { flex: 1; }
  .field { border-top: 2px solid var(--rule); padding: 8px 10px 10px; height: 78px; }
  .details-roast .field { height: 88px; padding-left: 16px; }
  .details-roast .field:first-child { border-top: none; }
  .field-label {
    font-size: 16px; text-transform: uppercase; color: var(--muted);
    letter-spacing: 0.5px;
  }
  .field-value { font-size: 21px; font-weight: 700; margin-top: 4px; white-space: nowrap; }
</style>
</head>
<body>
  <div class="label">
    <div class="sticker">
      <div class="branch-illustration" role="img" aria-label="Engraved illustration of a coffee branch with leaves, cherries and two roasted beans"></div>
      <h1 class="product-name">Moruvi<br>Kelano<br>AA</h1>
      <div class="process-tag"><span>Washed &amp;</span><span>Natural</span></div>
      <div class="details">
        <div class="details-origin">
          <div class="field">
            <div class="field-label">Origins:</div>
            <div class="field-value">Mt. Elgon, Trans-Nzoia County, Kenya</div>
          </div>
          <div class="field">
            <div class="field-label">Coffee variety:</div>
            <div class="field-value">100 % Arabica</div>
          </div>
          <div class="field">
            <div class="field-label">Growing altitude:</div>
            <div class="field-value">Altitude: 1 800 amsl</div>
          </div>
        </div>
        <div class="details-roast">
          <div class="field">
            <div class="field-label">Roast date</div>
            <div class="field-value">00.00.00</div>
          </div>
          <div class="field">
            <div class="field-label">Best before</div>
            <div class="field-value">00.00.00</div>
          </div>
          <div class="field">
            <div class="field-label">Roasted by</div>
            <div class="field-value">Rans-Nzoia County</div>
          </div>
        </div>
      </div>
    </div>
  </div>
</body>
</html>
```